Post card for landscape service

Velbrin Estate Management**FEATURED SERVICE*** Weekly Lawn mowing service starting at $15/ cutting ****other services****landscape servicespring and fall clean uplawn and flowerbed care (pest and weed control)fertilizing plantingand moreCall for a Free estimate!!10% off first months service with signed contract

Please make double sided ( a front and a back)

Target Market(s)

home owners

Industry/Entity Type

Landscape

Requirements
Must have
• please feture the weekly lawn mowing service and then list the other sevices
• contact info... can be found on business card that was uploaded.
• must say residential services
Should not have
• please dont list reo management

```html
<!DOCTYPE html>
<html lang="en">
<head>
<meta charset="utf-8">
<title>Velbrin Residential Services – Postcard</title>
<link href="https://fonts.googleapis.com/css2?family=Montserrat:wght@400;500;600&family=Oswald:wght@500&family=Roboto+Condensed:wght@400;700&display=swap" rel="stylesheet">
<style>
  :root {
    --grass-light: #4f9a2c;
    --grass-mid: #2f6f1a;
    --grass-dark: #0c2a08;
    --cream: #fbf0dc;
    --white: #ffffff;
  }
  * { margin: 0; padding: 0; box-sizing: border-box; }
  html, body { width: 848px; height: 1200px; overflow: hidden; background: var(--grass-dark); }
  .postcard {
    position: relative;
    width: 848px;
    height: 1200px;
    overflow: hidden;
    color: var(--white);
  }
  .lawn-backdrop {
    position: absolute;
    inset: 0;
    background:
      radial-gradient(ellipse 70% 45% at 50% 30%, var(--grass-light) 0%, var(--grass-mid) 55%, transparent 100%),
      linear-gradient(180deg, var(--grass-mid) 0%, #1e5212 50%, var(--grass-dark) 100%);
  }
  .brand-mark {
    position: absolute;
    left: 334px;
    top: 300px;
    width: 180px;
    height: 180px;
    border-radius: 50%;
    background: var(--cream);
  }
  .brand-name {
    position: absolute;
    top: 618px;
    width: 100%;
    text-align: center;
    font-family: "Montserrat", sans-serif;
    font-weight: 600;
    font-size: 112px;
    line-height: 1;
    letter-spacing: 1px;
    color: var(--cream);
  }
  .brand-tagline {
    position: absolute;
    top: 726px;
    width: 100%;
    text-align: center;
    font-family: "Montserrat", sans-serif;
    font-weight: 400;
    font-size: 20px;
    letter-spacing: 12.5px;
    padding-left: 12px;
    color: var(--white);
  }
  .featured-service {
    position: absolute;
    top: 838px;
    width: 100%;
    text-align: center;
    font-family: "Montserrat", sans-serif;
    font-weight: 500;
    font-size: 27px;
    letter-spacing: -0.3px;
  }
  .featured-service em { font-weight: 400; font-size: 25px; }
  .service-list {
    position: absolute;
    top: 890px;
    left: 106px;
    width: 632px;
    height: 52px;
    display: flex;
    list-style: none;
    border-left: 1.5px solid var(--white);
    border-right: 1.5px solid var(--white);
  }
  .service-list li {
    display: flex;
    align-items: center;
    justify-content: center;
    text-align: center;
    font-family: "Oswald", sans-serif;
    font-weight: 500;
    font-size: 21px;
    line-height: 1.15;
    text-transform: uppercase;
    letter-spacing: -0.5px;
  }
  .service-list li + li { border-left: 1.5px solid var(--white); }
  .service-list li:nth-child(1) { width: 112px; }
  .service-list li:nth-child(2) { width: 194px; }
  .service-list li:nth-child(3) { width: 128px; }
  .service-list li:nth-child(4) { width: 198px; }
  .offer-price {
    position: absolute;
    top: 982px;
    width: 100%;
    text-align: center;
    font-family: "Montserrat", sans-serif;
    font-weight: 500;
    font-size: 21px;
    color: var(--cream);
  }
  .offer-discount {
    position: absolute;
    top: 1014px;
    width: 100%;
    text-align: center;
    font-family: "Roboto Condensed", sans-serif;
    font-size: 19px;
  }
  .contact-invite {
    position: absolute;
    top: 1076px;
    width: 100%;
    text-align: center;
    font-family: "Roboto Condensed", sans-serif;
    font-size: 22px;
  }
  .contact-details {
    position: absolute;
    top: 1106px;
    width: 100%;
    text-align: center;
    font-family: "Roboto Condensed", sans-serif;
    font-size: 30px;
    letter-spacing: -0.3px;
  }
  .offer-discount strong, .contact-invite strong, .contact-details strong { font-weight: 700; }
</style>
</head>
<body>
  <main class="postcard">
    <div class="lawn-backdrop" role="img" aria-label="Close-up photograph of a lush green lawn"></div>

    <div class="brand-mark"></div>
    <h1 class="brand-name">VELBRIN</h1>
    <p class="brand-tagline">RESIDENTIAL SERVICES</p>

    <p class="featured-service">WEEKLY LAWN MOWING SERVICE <em>and</em></p>

    <ul class="service-list">
      <li>Pest<br>Control</li>
      <li>Landscape<br>Maintenance</li>
      <li>Snow<br>Removal</li>
      <li>Spring &amp; Fall<br>Clean Up</li>
    </ul>

    <p class="offer-price">Weekly mowing starting at $15 per cutting</p>
    <p class="offer-discount"><strong>10% OFF</strong> your first month's service with a signed contract</p>

    <p class="contact-invite">For a <strong>FREE</strong> quote or more information...</p>
    <p class="contact-details">call <strong>(908) 555-0142</strong> or email <strong>VelbrinEstate@mailbox.com</strong></p>
  </main>
</body>
</html>
```